Larkfield Medical Rooms - Websit, online payment facility and patient information portal

We are a small specialist medical centre inNewcastle NSW, Australia. We would like a modern, open easy to navigate (we have many elderly clients) webpage for our customers to use. We would like a page for content uploads (like referrals etc), an enquiry page, and some patient information pages.

Our logo is attached. We would like a modern, grey scale or black and white website for our customers to use. The landing page should have high resolution images and use san serif font.

Target Market(s)

General Audience, Modern

Industry/Entity Type

Health And Wellness

Coding

Coded - Design and coding required

Number of Pages Required

5+ page

Font styles to use
Sans Serif

Colors
cbcbcb
757575
7f7f7f
c4c4c4
85cae6
cee9f5
cfdfed

Requirements
Must have
• Landing Page
• Several Other pages for content upload
• Ability to do online payments
• Enquiry form
• Contact page
• Social Media Links

```html
<!DOCTYPE html>
<html lang="en">
<head>
<meta charset="utf-8">
<title>Larkfield Medical Rooms</title>
<link href="https://fonts.googleapis.com/css2?family=Oswald:wght@300;400;600&family=Open+Sans:wght@400;600&display=swap" rel="stylesheet">
<style>
  :root{
    --ink:#2b2b2b;
    --text:#555555;
    --mid:#7f7f7f;
    --soft:#c4c4c4;
    --pale:#e6e6e6;
    --band:#ececec;
    --paper:#ffffff;
  }
  *{box-sizing:border-box;margin:0;padding:0}
  html,body{width:1200px;height:1200px;overflow:hidden;background:var(--paper)}
  body{position:relative;font-family:"Open Sans",Arial,sans-serif;color:var(--text)}
  .page{position:absolute;left:426px;top:0;width:348px;height:1200px;overflow:hidden}
  .abs{position:absolute}
  .display{font-family:"Oswald",Arial,sans-serif;font-weight:300;color:var(--ink);letter-spacing:3px;line-height:1;white-space:nowrap}
  .kicker{font-family:"Oswald",Arial,sans-serif;font-weight:600;color:var(--ink);font-size:8px;letter-spacing:2px;line-height:1;white-space:nowrap}
  .copy{font-size:3.6px;line-height:5.3px;color:var(--text)}
  .copy p+p{margin-top:5px}
  .btn{position:absolute;background:var(--ink);color:#fff;font-family:"Oswald",Arial,sans-serif;font-size:3.4px;letter-spacing:.3px;display:flex;align-items:center;justify-content:center;text-transform:uppercase}
  .mark-dot{position:absolute;width:10px;height:10px;border-radius:50%;background:var(--ink)}
  .tree-panel{position:absolute}
  .tree-right{background:linear-gradient(to left,#e9e9e9 0%,#f3f3f3 55%,rgba(255,255,255,0) 100%)}
  .tree-left{background:linear-gradient(to right,#e9e9e9 0%,#f3f3f3 55%,rgba(255,255,255,0) 100%)}
  .photo{position:absolute}
  .social{display:flex;gap:1.5px}
  .social span{width:6px;height:6px;border-radius:50%;background:var(--ink);display:block}
  .topphone{font-size:4px;color:var(--ink);display:flex;align-items:center;gap:3px;letter-spacing:.3px}
  .hero{left:0;top:10px;width:348px;height:198px;background:
      linear-gradient(115deg,rgba(255,255,255,0) 0%,rgba(255,255,255,0) 42%,rgba(120,120,120,.35) 42%,rgba(120,120,120,.35) 58%,rgba(255,255,255,0) 58%),
      linear-gradient(135deg,#e4e4e4 0%,#d0d0d0 40%,#c2c2c2 70%,#d6d6d6 100%)}
  .nav{left:26px;top:28px;width:294px;height:21px;background:#fff;box-shadow:0 1px 3px rgba(0,0,0,.3);display:flex;align-items:center;padding-left:10px;gap:4px;font-family:"Oswald",Arial,sans-serif;font-size:3.6px;color:var(--ink);letter-spacing:.2px;white-space:nowrap}
  .nav .sep{color:var(--mid)}
  .hero-name{left:0;width:348px;top:128px;text-align:center}
  .hero-name .big{font-family:"Oswald",Arial,sans-serif;font-weight:300;font-size:21px;color:var(--ink);letter-spacing:1px;line-height:1}
  .hero-name .small{font-family:"Oswald",Arial,sans-serif;font-weight:300;font-size:9px;color:#4a4a4a;letter-spacing:3px;line-height:1;margin-top:1px}
  .svc{position:absolute;width:62px;text-align:center}
  .svc .ico{width:28px;height:28px;border-radius:50%;background:var(--ink);margin:0 auto;display:flex;align-items:center;justify-content:center}
  .svc h3{font-family:"Oswald",Arial,sans-serif;font-weight:600;font-size:5px;letter-spacing:1px;color:var(--ink);margin-top:11px;line-height:1}
  .svc p{font-size:3.5px;line-height:4.8px;margin-top:3px;color:var(--text)}
  .divider{position:absolute;top:700px;width:1px;height:35px;background:var(--pale)}
  .field{position:absolute;border:.8px solid #9a9a9a;background:#fff;font-family:"Oswald",Arial,sans-serif;font-size:3.3px;color:var(--ink);padding:2px 5px;letter-spacing:.2px}
  .footer{left:0;top:1152px;width:348px;height:30px;background:var(--band)}
  .finfo{position:absolute;font-size:3.5px;line-height:4.8px;color:var(--text);display:flex;align-items:center;gap:5px}
  .legal{left:26px;top:1190px;font-family:"Oswald",Arial,sans-serif;font-size:3.4px;letter-spacing:.5px;color:var(--ink)}
</style>
</head>
<body>
<main class="page">

  <div class="abs social" style="left:26px;top:1px"><span></span><span></span><span></span><span></span><span></span></div>
  <div class="abs topphone" style="left:282px;top:1px">
    <svg width="5" height="5" viewBox="0 0 24 24"><path d="M6.6 10.8a15 15 0 0 0 6.6 6.6l2.2-2.2a1 1 0 0 1 1-.25 11.4 11.4 0 0 0 3.6.6 1 1 0 0 1 1 1V20a1 1 0 0 1-1 1A17 17 0 0 1 3 4a1 1 0 0 1 1-1h3.5a1 1 0 0 1 1 1c0 1.25.2 2.45.57 3.57a1 1 0 0 1-.25 1z" fill="#2b2b2b"/></svg>
    02 4955 0183
  </div>

  <div class="abs hero photo" role="img" aria-label="Greyscale photograph of the clinic entrance with the street number beside the door"></div>
  <nav class="abs nav">
    <span>HOME</span><span class="sep">|</span>
    <span>COLONOSCOPY</span><span class="sep">|</span>
    <span>GASTROSCOPY</span><span class="sep">|</span>
    <span>CAPSULE ENDOSCOPY</span><span class="sep">|</span>
    <span>PATIENT INFORMATION SHEETS</span><span class="sep">|</span>
    <span>CONTACT DETAILS</span><span class="sep">|</span>
    <svg width="5" height="5" viewBox="0 0 24 24"><circle cx="10" cy="10" r="6" fill="none" stroke="#2b2b2b" stroke-width="3"/><path d="M15 15l6 6" stroke="#2b2b2b" stroke-width="3"/></svg>
  </nav>
  <div class="abs hero-name">
    <div class="big">LARKFIELD</div>
    <div class="small">Medical Rooms</div>
  </div>

  <div class="tree-panel tree-right" role="img" aria-label="Faint decorative tree" style="left:276px;top:208px;width:72px;height:166px"></div>
  <div class="photo" role="img" aria-label="Black and white photograph of a long hallway with timber floor" style="left:14px;top:194px;width:130px;height:185px;background:linear-gradient(90deg,#262626 0%,#3c3c3c 30%,#8c8c8c 46%,#b0b0b0 50%,#8c8c8c 54%,#3c3c3c 70%,#262626 100%);box-shadow:0 2px 4px rgba(0,0,0,.35)"></div>
  <div class="mark-dot" style="left:162px;top:231px"></div>
  <div class="abs kicker" style="left:162px;top:251px">WELCOME TO</div>
  <div class="abs display" style="left:162px;top:264px;font-size:25px;letter-spacing:2.5px">LARKFIELD</div>
  <div class="abs copy" style="left:162px;top:297px;width:160px">
    <p>Our specialist rooms offer calm, unhurried care for every patient who walks through our door. We keep appointments simple, clear and on time, and our team takes the time to explain each step of your procedure, so you always know what to expect before, during and after your visit.</p>
    <p>Referral forms, patient information sheets and online payments are all available here, any time of day, from home.</p>
  </div>
  <div class="btn" style="left:162px;top:357px;width:45px;height:11px">Contact Us</div>

  <div class="tree-panel tree-left" role="img" aria-label="Faint decorative tree" style="left:0;top:428px;width:60px;height:158px"></div>
  <div class="mark-dot" style="left:27px;top:443px"></div>
  <div class="abs kicker" style="left:26px;top:465px">ABOUT</div>
  <div class="abs display" style="left:26px;top:477px;font-size:25px;letter-spacing:2.5px">LARKFIELD</div>
  <div class="abs copy" style="left:26px;top:511px;width:160px">
    <p>Larkfield Medical Rooms is a small specialist centre in Newcastle, NSW. Our team focuses on gentle, modern procedures, clear explanations and a quiet, welcoming space for patients of every age, including many who have been with us for years.</p>
    <p>We welcome new referrals from local doctors and are always happy to answer questions by phone.</p>
  </div>
  <div class="btn" style="left:26px;top:570px;width:45px;height:12px">Learn More</div>
  <div class="photo" role="img" aria-label="Black and white portrait of the lead specialist" style="left:202px;top:414px;width:129px;height:187px;background:linear-gradient(180deg,#fafafa 0%,#e2e2e2 30%,#c8c8c8 60%,#e8e8e8 100%);border:1px solid #dcdcdc;box-shadow:0 2px 4px rgba(0,0,0,.3)"></div>

  <div class="mark-dot" style="left:169px;top:632px"></div>
  <div class="abs kicker" style="left:0;width:348px;text-align:center;top:655px">LARKFIELD</div>
  <div class="abs display" style="left:0;width:348px;text-align:center;top:667px;font-size:25px">OUR SERVICES</div>
  <div class="divider" style="left:98px"></div>
  <div class="divider" style="left:174px"></div>
  <div class="divider" style="left:251px"></div>
  <div class="svc" style="left:28px;top:704px">
    <div class="ico"><svg width="14" height="14" viewBox="0 0 24 24" fill="none" stroke="#fff" stroke-width="1.4"><path d="M12 3v18M7 6h10M8 10c2 1 6 1 8 0M9 14c2 1 4 1 6 0"/></svg></div>
    <h3>YOUR HEADING</h3><p>Gentle, thorough care from our experienced specialists.</p>
  </div>
  <div class="svc" style="left:105px;top:704px">
    <div class="ico"><svg width="14" height="14" viewBox="0 0 24 24" fill="none" stroke="#fff" stroke-width="1.4"><path d="M9 3h6v6h6v6h-6v6H9v-6H3V9h6z"/></svg></div>
    <h3>YOUR HEADING</h3><p>Gentle, thorough care from our experienced specialists.</p>
  </div>
  <div class="svc" style="left:181px;top:704px">
    <div class="ico"><svg width="14" height="14" viewBox="0 0 24 24" fill="none" stroke="#fff" stroke-width="1.4"><path d="M12 20s-8-5-8-11a4 4 0 0 1 8-1 4 4 0 0 1 8 1c0 6-8 11-8 11z"/><path d="M4 12h5l1.5-3 2 6 1.5-3H20"/></svg></div>
    <h3>YOUR HEADING</h3><p>Gentle, thorough care from our experienced specialists.</p>
  </div>
  <div class="svc" style="left:257px;top:704px">
    <div class="ico"><svg width="14" height="14" viewBox="0 0 24 24" fill="none" stroke="#fff" stroke-width="1.4"><path d="M6 3v6a5 5 0 0 0 10 0V3M11 14v2a4 4 0 0 0 8 0v-3"/><circle cx="19" cy="11" r="2"/></svg></div>
    <h3>YOUR HEADING</h3><p>Gentle, thorough care from our experienced specialists.</p>
  </div>

  <div class="photo" role="img" aria-label="Soft greyscale photograph of the waiting room" style="left:0;top:794px;width:348px;height:140px;background:linear-gradient(180deg,rgba(255,255,255,0) 60%,rgba(150,150,150,.35) 100%),linear-gradient(90deg,#bababa 0%,#d6d6d6 30%,#e4e4e4 60%,#d2d2d2 100%)"></div>
  <div class="mark-dot" style="left:169px;top:830px"></div>
  <div class="abs display" style="left:0;width:348px;text-align:center;top:851px;font-size:16px;letter-spacing:.5px;font-weight:400;color:#333">YOUR HEADING GOES HERE</div>
  <div class="abs copy" style="left:92px;top:871px;width:164px;text-align:center;line-height:5px">Book your appointment online in just a few minutes. Our friendly staff will confirm your visit and send you everything you need to prepare.</div>
  <div class="btn" style="left:150px;top:895px;width:46px;height:11px">Book Now</div>

  <div class="tree-panel tree-right" role="img" aria-label="Faint decorative tree" style="left:258px;top:1000px;width:90px;height:132px"></div>
  <div class="mark-dot" style="left:169px;top:964px"></div>
  <div class="abs kicker" style="left:0;width:348px;text-align:center;top:988px">LARKFIELD</div>
  <div class="abs display" style="left:0;width:348px;text-align:center;top:1000px;font-size:25px">CONTACT US</div>
  <div class="field" style="left:45px;top:1042px;width:126px;height:12px">NAME</div>
  <div class="field" style="left:45px;top:1059px;width:126px;height:12px">EMAIL</div>
  <div class="field" style="left:45px;top:1076px;width:126px;height:12px">PHONE</div>
  <div class="field" style="left:45px;top:1093px;width:126px;height:12px">SUBJECT</div>
  <div class="field" style="left:176px;top:1042px;width:127px;height:63px">COMMENTS</div>
  <div class="btn" style="left:151px;top:1118px;width:45px;height:12px">Submit</div>

  <div class="abs footer"></div>
  <div class="finfo" style="left:45px;top:1157px">
    <svg width="7" height="9" viewBox="0 0 24 30" fill="none" stroke="#555" stroke-width="2"><path d="M12 28s9-10 9-17a9 9 0 0 0-18 0c0 7 9 17 9 17z"/><circle cx="12" cy="11" r="3"/></svg>
    <span style="width:70px">Larkfield Medical Rooms,<br>12 Hunter Street,<br>Newcastle NSW 2300</span>
  </div>
  <div class="finfo" style="left:157px;top:1163px">
    <svg width="9" height="7" viewBox="0 0 30 22" fill="none" stroke="#555" stroke-width="2"><rect x="1" y="1" width="28" height="20"/><path d="M1 1l14 11L29 1"/></svg>
    <span>info@larkfieldrooms.com.au</span>
  </div>
  <div class="finfo" style="left:263px;top:1163px">
    <svg width="7" height="7" viewBox="0 0 24 24"><path d="M6.6 10.8a15 15 0 0 0 6.6 6.6l2.2-2.2a1 1 0 0 1 1-.25 11.4 11.4 0 0 0 3.6.6 1 1 0 0 1 1 1V20a1 1 0 0 1-1 1A17 17 0 0 1 3 4a1 1 0 0 1 1-1h3.5a1 1 0 0 1 1 1c0 1.25.2 2.45.57 3.57a1 1 0 0 1-.25 1z" fill="none" stroke="#555" stroke-width="2"/></svg>
    <span>02 4955 0183</span>
  </div>
  <div class="abs legal">COPYRIGHT © 2017 LARKFIELD ALL RIGHTS RESERVED</div>
  <div class="abs social" style="left:279px;top:1189px"><span style="background:var(--mid)"></span><span style="background:var(--mid)"></span><span style="background:var(--mid)"></span><span style="background:var(--mid)"></span><span style="background:var(--mid)"></span></div>

</main>
</body>
</html>
```